Talent Management Company Needs Business Cards

Using one of the logos provided (attached) K&R Talent Collective needs a business card designed.
Please visit our website for more information about us-

www.krtalentcollective.example

The face should feature a dramatic presentation of the logo with the back being reserved for our professional information which is:

The information should be:
Dorian T. Vickers
C.E.O
Email: dtvickers@krtalentcollective.example
Mobile: 555-804-2917
Website: www.krtalentcollective.example

Marcus L. Vickers
Director of Public Relations
Email: mlvickers@krtalentcollective.example
Mobile: 555-806-3350

Jules R. Hampton
Director of Client Development
Email: jhampton@krtalentcollective.example

Simon Hurlock
Director of Brand Development
Email: shurlock@krtalentcollective.example

Would like the logo to have color. I would like to see one side red or black and the other side white but if it looks better in either black or red that would be fine to but would like to see how it comes out.

Please feel free to message me and if you would like just the icon alone I have other image files that I can send as well.

Target Market(s)

Professional Athletes, coaches, entertainers age 18-35 but also must be accepted in the business community

Industry/Entity Type

Business

Requirements
Must have
• 1) Use the logo
2) Double sided
3) Distinctive
Nice to have
• Small simple images for telephone, e-mail, and Url.

```html
<!DOCTYPE html>
<html lang="en">
<head>
<meta charset="utf-8">
<title>K&amp;R Talent Collective – Business Card</title>
<link rel="stylesheet" href="https://fonts.googleapis.com/css2?family=Arimo:wght@400;700&family=Marcellus&display=swap">
<style>
  :root {
    --page: #ffffff;
    --red-bright: #ec1c27;
    --red-deep: #7d0309;
    --charcoal: #2b2b2b;
    --ink: #231f20;
    --text: #3a3a3a;
    --white: #ffffff;
    --rule: #555555;
  }
  * { margin: 0; padding: 0; box-sizing: border-box; }
  html, body {
    width: 1200px; height: 901px; overflow: hidden;
    background: var(--page);
  }
  .canvas { position: relative; width: 1200px; height: 901px; }

  .card {
    position: absolute; left: 272px; width: 628px; height: 360px;
    overflow: hidden;
    box-shadow: 4px 5px 8px rgba(0,0,0,0.35);
  }
  .card--front {
    top: 53px;
    background: radial-gradient(ellipse 70% 75% at 50% 35%, var(--red-bright) 0%, #c8101a 50%, var(--red-deep) 100%);
  }
  .card--back { top: 468px; background: var(--white); }

  .brand-mark {
    position: absolute; left: 50%; top: 95px;
    width: 86px; height: 86px; margin-left: -43px;
    border-radius: 50%;
  }
  .card--front .brand-mark { background: var(--charcoal); }
  .card--back .brand-mark { background: var(--red-bright); top: 40px; }

  .brand-name {
    position: absolute; left: 0; right: 0; top: 200px;
    text-align: center;
    font-family: "Marcellus", serif;
    font-size: 31px; letter-spacing: 0.5px;
    white-space: nowrap;
  }
  .card--front .brand-name { color: var(--white); }
  .card--back .brand-name { color: var(--ink); top: 142px; }

  .url-tab {
    position: absolute; left: 115px; width: 396px; height: 39px; bottom: 0;
  }
  .url-tab svg { position: absolute; inset: 0; }
  .url-tab span {
    position: relative; display: block; text-align: center;
    font-family: "Arimo", sans-serif; font-size: 16px; line-height: 39px;
    color: var(--white);
  }
  .card--back .url-tab { bottom: 0; }

  .red-strip {
    position: absolute; left: 0; right: 0; bottom: 0; height: 19px;
    background: linear-gradient(90deg, #b10a12, var(--red-bright) 50%, #b10a12);
  }

  .contact-person {
    position: absolute; right: 387px; top: 258px; text-align: right;
    font-family: "Arimo", sans-serif;
  }
  .contact-person .name { color: var(--red-bright); font-weight: 700; font-size: 18px; line-height: 22px; }
  .contact-person .title { color: var(--text); font-size: 15px; line-height: 22px; }

  .contact-rule {
    position: absolute; left: 259px; top: 258px; width: 2px; height: 46px;
    background: var(--rule);
  }
  .contact-lines {
    position: absolute; left: 276px; top: 258px;
    font-family: "Arimo", sans-serif; font-size: 16px; color: var(--text);
    list-style: none;
  }
  .contact-lines li { display: flex; align-items: center; height: 22px; white-space: nowrap; }
  .contact-lines svg { width: 12px; height: 12px; margin-right: 8px; flex: none; }
</style>
</head>
<body>
<main class="canvas">

  <section class="card card--front" aria-label="Card front">
    <div class="brand-mark"></div>
    <p class="brand-name">K&amp;R TALENT COLLECTIVE</p>
    <div class="url-tab">
      <svg viewBox="0 0 396 39" preserveAspectRatio="none"><polygon points="26,0 370,0 396,39 0,39" fill="#2b2b2b"/></svg>
      <span>www.krtalentcollective.example</span>
    </div>
  </section>

  <section class="card card--back" aria-label="Card back">
    <div class="brand-mark"></div>
    <p class="brand-name">K&amp;R TALENT COLLECTIVE</p>

    <div class="contact-person">
      <p class="name">Dorian T. Vickers</p>
      <p class="title">C.E.O</p>
    </div>
    <div class="contact-rule"></div>
    <ul class="contact-lines">
      <li>
        <svg viewBox="0 0 12 12"><rect x="3" y="0.5" width="6" height="11" rx="1" fill="none" stroke="#ec1c27" stroke-width="1.4"/><rect x="4.5" y="2" width="3" height="6" fill="#ec1c27"/></svg>
        555-804-2917
      </li>
      <li>
        <svg viewBox="0 0 12 12"><rect x="0.5" y="2.5" width="11" height="7.5" fill="#ec1c27"/><polyline points="0.5,2.5 6,7 11.5,2.5" fill="none" stroke="#ffffff" stroke-width="1"/></svg>
        dtvickers@krtalentcollective.example
      </li>
    </ul>

    <div class="red-strip"></div>
    <div class="url-tab">
      <svg viewBox="0 0 396 39" preserveAspectRatio="none"><polygon points="26,0 370,0 396,39 0,39" fill="#2b2b2b"/></svg>
      <span>www.krtalentcollective.example</span>
    </div>
  </section>

</main>
</body>
</html>
```